Ad for Cyber Security Company- Print Ad

We are looking for an awesome designer to create a one page advertisement for the Brimox Security data analytics platform that will be featured in an upcoming security magazine. This is also going to be featured in an upcoming trade show. Brimox Security produced the BRIMOX platform to help companies unify their security environment and help them address Insider Threat, Fraud and Anomaly ID and resolution. BRIMOX uses an an advanced ingestion engine, machine learning, and workflow automation to ensure the right people are getting the right info at the right time. We serve enterprise level customers, augmenting and enhancing, not replacing their existing security stack. We would like few or single image, clean, and open ad built around the tagline 'Make Security a Team Sport.' We would like the logo to be featured, and include our website address on the page (www.brimoxsecurity.net). See below for style guide.

Target Market(s)

Industry insiders, Chief Information Security Officers (CISO) and Technical directors.

Other font styles liked:
• See style guide, but we are open to suggestion.

Requirements
Must have
• A single image (minimum), Feature the provided logo, Include the tagline 'Make Security a Team Sport' and have the website somewhere on the ad. The image should focus on the conveying the message of "Make Security a Team Sport" and not be a generic security (padlock, network, etc.) image.
• See included style guide.

```html
<!DOCTYPE html>
<html lang="en">
<head>
<meta charset="utf-8">
<title>Brimox Security – Make Security a Team Sport</title>
<link href="https://fonts.googleapis.com/css2?family=Fira+Sans:wght@600;700;800&family=Open+Sans:wght@400;600&display=swap" rel="stylesheet">
<style>
  :root{
    --orange:#f26522;
    --charcoal:#3b3b3d;
    --ink:#1d1f24;
    --steel:#55565a;
    --paper:#ffffff;
    --backdrop:#c9c9c9;
    --text-dark:#222;
  }
  html,body{margin:0;padding:0;width:1200px;height:1200px;overflow:hidden;background:var(--backdrop);}
  .flyer{
    position:absolute;left:153px;top:26px;width:744px;height:956px;
    transform:scale(1.2);transform-origin:0 0;
    background:var(--paper);overflow:hidden;
    font-family:"Open Sans",sans-serif;color:var(--text-dark);
    box-shadow:0 6px 18px rgba(0,0,0,.25);
  }
  .flyer svg.art{position:absolute;left:0;top:0;}
  .brand{position:absolute;left:30px;top:28px;display:flex;align-items:center;gap:12px;}
  .brand-mark{width:46px;height:46px;background:var(--orange);}
  .brand-name{font-family:"Fira Sans",sans-serif;font-weight:800;font-size:27px;line-height:26px;color:var(--charcoal);letter-spacing:1px;}
  .tagline{position:absolute;right:30px;top:392px;text-align:right;font-family:"Fira Sans",sans-serif;font-weight:700;font-size:44px;line-height:52px;}
  .tagline .lead{color:var(--orange);}
  .tagline .rest{color:var(--paper);}
  .intro{position:absolute;left:28px;top:577px;width:297px;color:var(--paper);}
  .intro h2{margin:0 0 14px;font-weight:400;font-size:17px;line-height:20px;text-align:justify;}
  .intro p{margin:0 0 18px;font-size:12.4px;line-height:14.3px;text-align:justify;}
  .about-tab{position:absolute;left:583px;top:562px;width:161px;height:40px;background:var(--orange);border-radius:20px 0 0 20px;
    color:var(--paper);font-family:"Fira Sans",sans-serif;font-weight:700;font-size:21px;line-height:40px;text-indent:31px;}
  .about{position:absolute;left:363px;top:622px;width:354px;}
  .about p{margin:0 0 13px;font-size:12.2px;line-height:14.2px;text-align:justify;}
  .phone{position:absolute;left:28px;top:898px;display:flex;align-items:center;gap:6px;
    font-family:"Fira Sans",sans-serif;font-weight:700;font-size:21px;color:var(--charcoal);letter-spacing:.5px;}
  .contact{position:absolute;left:383px;top:890px;color:var(--paper);font-size:15.5px;line-height:21px;}
  .contact div{display:flex;align-items:center;gap:8px;}
</style>
</head>
<body>
<div class="flyer">
  <svg class="art" width="744" height="956" viewBox="0 0 744 956">
    <defs>
      <linearGradient id="heroTone" x1="0" y1="0" x2="1" y2="1">
        <stop offset="0" stop-color="#2f4a66"/>
        <stop offset=".45" stop-color="#3d4f63"/>
        <stop offset=".75" stop-color="#1e232c"/>
        <stop offset="1" stop-color="#14161b"/>
      </linearGradient>
    </defs>
    <!-- lower left panel, sits beneath the hero curve -->
    <path d="M0,320 H342 V800 Q342,840 302,840 H0 Z" fill="var(--charcoal)"/>
    <!-- hero photo zone -->
    <path role="img" aria-label="Photo of two analysts working together at a computer in a security operations centre" d="M0,100 H744 V470 C420,560 150,480 0,330 Z" fill="url(#heroTone)"/>
    <!-- swoosh stripes under hero -->
    <path d="M0,330 C150,480 420,560 744,470" fill="none" stroke="var(--steel)" stroke-width="12"/>
    <path d="M0,346 C150,500 420,576 744,484" fill="none" stroke="var(--orange)" stroke-width="6"/>
    <!-- product circle -->
    <circle cx="615" cy="110" r="282" fill="#49494c" stroke="var(--orange)" stroke-width="9"/>
    <rect role="img" aria-label="Desktop monitor displaying the analytics dashboard" x="412" y="78" width="305" height="236" rx="6" fill="#8b8d92"/>
    <!-- header -->
    <path d="M0,0 H470 C430,80 320,128 0,138 Z" fill="var(--orange)"/>
    <path d="M0,0 H455 C415,72 310,118 0,128 Z" fill="var(--paper)"/>
    <!-- footer -->
    <rect x="0" y="935" width="744" height="21" fill="var(--orange)"/>
    <path d="M362,956 V905 Q362,885 382,885 H744 V956 Z" fill="var(--orange)"/>
    <circle cx="667" cy="912" r="13" fill="var(--paper)"/>
    <circle cx="702" cy="912" r="13" fill="var(--paper)"/>
  </svg>

  <div class="brand">
    <div class="brand-mark"></div>
    <div class="brand-name">BRIMOX<br>SECURITY</div>
  </div>

  <div class="tagline"><div class="lead">Make Security</div><div class="rest">a Team Sport</div></div>

  <section class="intro">
    <h2>BRIMOX is a security data analytics platform, enabling security teams and business partners with timely, actionable alerts and intelligence.</h2>
    <p>BRIMOX moves as fast as you. With a variety of deployment models including on-premises, hybrid, or fully cloud-based, clients measure ROI in weeks, not months.</p>
    <p>BRIMOX makes security a team sport. Leveraging advanced machine learning and workflow optimization, BRIMOX ensures that the right information is making it to the right people every time.</p>
  </section>

  <div class="about-tab">About Us</div>
  <section class="about">
    <p>BRIMOX security data analytics platform that will be featured in an upcoming security magazine. This is also going to be featured in an upcoming trade show.</p>
    <p>Brimox Security produced the BRIMOX platform to help companies unify their security environment and help them address Insider Threat, Fraud and Anomaly ID and resolution.</p>
    <p>BRIMOX uses an an advanced ingestion engine, machine learning, and workflow automation to ensure the right people are getting the right info at the right time. We serve enterprise level customers, augmenting and enhancing, not replacing their existing security stack.</p>
    <p>BRIMOX complements existing tools, including SIEM and UBA, to provide enhanced visibility into your organization’s blind spots.</p>
  </section>

  <div class="phone">
    <svg width="17" height="17" viewBox="0 0 17 17" aria-hidden="true"><circle cx="8.5" cy="8.5" r="8.5" fill="var(--orange)"/><path d="M5.5,4.5 l2,0 l.8,2.4 -1.2,.9 q.9,1.9 2.6,2.7 l.9,-1.2 2.4,.8 0,2 q-5.5,.6 -7.5,-7.6z" fill="#fff"/></svg>
    IPSUM QUIA DOLOR
  </div>

  <div class="contact">
    <div><svg width="13" height="13" viewBox="0 0 13 13" aria-hidden="true"><circle cx="6.5" cy="6.5" r="5.5" fill="none" stroke="#fff" stroke-width="1.6"/><rect x="3.5" y="5" width="6" height="3.5" fill="#fff"/></svg>ipsumquiadolorsitamet</div>
    <div><svg width="13" height="13" viewBox="0 0 13 13" aria-hidden="true"><circle cx="6.5" cy="6.5" r="5.5" fill="none" stroke="#fff" stroke-width="1.2"/><ellipse cx="6.5" cy="6.5" rx="2.4" ry="5.5" fill="none" stroke="#fff" stroke-width="1"/><line x1="1" y1="6.5" x2="12" y2="6.5" stroke="#fff" stroke-width="1"/></svg>www.brimoxsecurity.net</div>
  </div>
</div>
</body>
</html>
```